Logo, letterhead and business card design for fun, different NYC consulting firm

THE BRACKENFIELD GROUP - We are looking for an identity package (logo, letterhead, business cards) that makes high-potential entrepreneurs and enterprising corporate executives trip over each other in their race to work with our startup "gurus." We coach and advise individuals (entrepreneurs and corporate executives) and consult organizations (startups and established companies) who want to unlock their entrepreneurial spirit so they can launch new ventures faster, with less investment and greater promise. On the big end, we helped Velonix rollout a new line of mobile accessories; on the small side, we helped a Florida woman start an elder care business that now employes 60 people.
Our President is a high-energy, generous guy. He's one of the most fun, approachable, and inspired millionaires I've ever met. His charisma alone makes entrepreneurs and executives of all stripes want to work with him-and these qualities are what we'd like to translate into our logo and other identity pieces.
Please, please, please don't go to the company's website to get a feel for us-the site is horrible, it's not our "vibe," and it's going to be re-imagined, stat!
Instead, know this:
we love startups
we are the home of creative ideas
we support entrepreneurs and enterprising corporate executives in everything they do
we create wealth and value
we help the world
The Brackenfield Group is composed of entrepreneur-gurus who are:
fun
independent
born to challenge
unconventional
practical
action-oriented
creative
balanced
Our tagline is:
Sparking the founder's drive | growing fresh ventures
Our business includes:
coaching | consulting | advisory
We plan on extending the winning identity to our website, so there may be more work in it for you beyond this initial package (more money, yeah!).
Our letterhead will be used almost exclusively as a background in Microsoft Word (we're not sure if we'll get it printed); and the business card should be double-sided, with an optional 2D barcode (if it works well into your design).
Updates
Dear designers -
Target Market(s)
People and organizations who are looking to launch new business ventures more quickly, affordably, and successfully than the competition
Industry/Entity Type
Investment
Requirements
Must have
- Business cards:
- company name: The Brackenfield Group
- web address: www.brackenfieldgroup-example.com
- physical address: 14 Brackenfield Way, Alderbrook, ST 00000
- name and title: Peter Holloway, President
- phone number: 203.555.0184
- e-mail address: pholloway@brackenfieldgroup-example.com
- tagline: Sparking the founder's drive | growing fresh ventures
- the card should be double-sided; on the back it should say: coaching | consulting | advisory (it's up to you if you want to put the company name and logo on the back and/or a QR code)
Letterhead:
- company name: The Brackenfield Group (along with coaching | consulting | advisory somewhere on the page)

```html
<!DOCTYPE html>
<html lang="en">
<head>
<meta charset="utf-8">
<title>The Brackenfield Group – Identity</title>
<link rel="stylesheet" href="https://fonts.googleapis.com/css2?family=Sanchez&display=swap">
<style>
  :root {
    --orange: #f05a28;
    --charcoal: #33363d;
    --slate: #77787b;
    --ink: #1f1f21;
    --paper: #ffffff;
    --edge: #c9c9c9;
    --shadow: rgba(0,0,0,0.28);
  }
  * { box-sizing: border-box; margin: 0; padding: 0; }
  html, body { width: 1200px; height: 1200px; overflow: hidden; background: var(--paper); }
  body { position: relative; font-family: "Sanchez", Georgia, serif; color: var(--charcoal); }

  .wordmark { position: absolute; line-height: 1.05; display: flex; align-items: flex-start; gap: 10px; white-space: nowrap; }
  .wordmark .mark-square { width: 12px; height: 12px; margin-top: 8px; flex: none; }
  .wordmark-primary { left: 60px; top: 150px; font-size: 36px; color: var(--orange); }
  .wordmark-primary .mark-square { background: var(--orange); }
  .wordmark-mono { left: 98px; top: 384px; font-size: 27px; color: var(--ink); }
  .wordmark-mono .mark-square { background: var(--ink); width: 10px; height: 10px; margin-top: 7px; }

  .sheet { position: absolute; background: var(--paper); border: 1px solid var(--edge); box-shadow: 3px 4px 6px var(--shadow); overflow: hidden; }

  .card-front { left: 54px; top: 670px; width: 288px; height: 184px; }
  .card-front .wordmark { left: 80px; top: 18px; font-size: 25px; color: var(--orange); }
  .card-front .wordmark .mark-square { background: var(--orange); width: 9px; height: 9px; margin-top: 7px; }

  .services { position: absolute; display: flex; align-items: center; gap: 6px; color: var(--charcoal); white-space: nowrap; }
  .services .dot { width: 6px; height: 6px; background: var(--orange); display: inline-block; }
  .card-front .services { right: 32px; bottom: 14px; font-size: 11.5px; }

  .card-back { left: 53px; top: 894px; width: 288px; height: 185px; }
  .name-tab { position: absolute; left: 18px; top: 39px; width: 171px; height: 31px; background: var(--orange); border-radius: 6px; color: var(--paper); font-size: 11.5px; display: flex; align-items: center; padding-left: 9px; gap: 5px; white-space: nowrap; }
  .name-tab .dot { width: 5px; height: 5px; background: var(--paper); }
  .contact-list { position: absolute; left: 19px; top: 91px; list-style: none; font-size: 9.5px; line-height: 13px; color: var(--ink); white-space: nowrap; }
  .contact-list li { display: flex; align-items: center; gap: 5px; }
  .contact-list .dot { width: 5px; height: 5px; background: var(--orange); flex: none; }
  .contact-list .web { color: var(--orange); padding-top: 2px; }
  .card-back .tagline-main { position: absolute; right: 24px; bottom: 10px; font-size: 9.5px; color: var(--slate); white-space: nowrap; }
  .card-back .tagline-side { position: absolute; left: 266px; top: 150px; transform-origin: 0 0; transform: rotate(-90deg); font-size: 9px; color: var(--slate); white-space: nowrap; }

  .letterhead { left: 390px; top: 78px; width: 712px; height: 1008px; }
  .letterhead .wordmark { left: 460px; top: 24px; font-size: 24px; color: var(--orange); }
  .letterhead .wordmark .mark-square { background: var(--orange); width: 9px; height: 9px; margin-top: 7px; }
  .letterhead .contact-list { left: 472px; top: 144px; font-size: 9.5px; line-height: 14px; }
  .letterhead .signatory { position: absolute; left: 472px; top: 192px; font-size: 10px; color: var(--orange); }
  .letterhead .tagline-side { position: absolute; left: 688px; top: 420px; transform-origin: 0 0; transform: rotate(-90deg); font-size: 10px; color: var(--slate); white-space: nowrap; }
  .letterhead .services { right: 42px; bottom: 22px; font-size: 12.5px; }
</style>
</head>
<body>

  <div class="wordmark wordmark-primary">
    <span class="mark-square"></span>
    <span>The<br>Brackenfield<br>Group</span>
  </div>

  <div class="wordmark wordmark-mono">
    <span class="mark-square"></span>
    <span>The<br>Brackenfield<br>Group</span>
  </div>

  <section class="sheet card-front" aria-label="Business card, front">
    <div class="wordmark">
      <span class="mark-square"></span>
      <span>The<br>Brackenfield<br>Group</span>
    </div>
    <p class="services">Mentoring <span class="dot"></span> Strategy <span class="dot"></span> Guidance</p>
  </section>

  <section class="sheet card-back" aria-label="Business card, back">
    <div class="name-tab">Peter Holloway <span class="dot"></span> President</div>
    <ul class="contact-list">
      <li><span class="dot"></span>203.555.0184</li>
      <li><span class="dot"></span>pholloway@brackenfieldgroup-example.com</li>
      <li><span class="dot"></span>14 Brackenfield Way, Alderbrook, ST 00000</li>
      <li class="web">www.brackenfieldgroup-example.com</li>
    </ul>
    <p class="tagline-side">| growing fresh ventures</p>
    <p class="tagline-main">Sparking the founder's drive</p>
  </section>

  <section class="sheet letterhead" aria-label="Letterhead">
    <div class="wordmark">
      <span class="mark-square"></span>
      <span>The<br>Brackenfield<br>Group</span>
    </div>
    <ul class="contact-list">
      <li><span class="dot"></span>14 Brackenfield Way, Alderbrook, ST 00000</li>
      <li><span class="dot"></span>203.555.0184</li>
      <li>www.brackenfieldgroup-example.com</li>
    </ul>
    <p class="signatory">Peter Holloway, President</p>
    <p class="tagline-side">Sparking the founder's drive | growing fresh ventures</p>
    <p class="services">Mentoring <span class="dot"></span> Strategy <span class="dot"></span> Guidance</p>
  </section>

</body>
</html>
```